Business card for Property Management consultant

I need a business card for my business LX Vantage - I consult to real estate agents to improve the performance of their Property Management departments (rental houses management). The card needs to be very professional looking, incorporating our logo and my photo plus the line "Develop your Rent Roll to Perform"

Target Market(s)

Real Estate business owners

Industry/Entity Type

Business Consultant

Contact Information for Business Card

Business name - LX Vantage (logo uploaded)
My Name : Marcia Kellaway -
Title : Property Management Consultant

Develop your Rent Roll to perform

Phone : +61 438592716
email : marcia@lxvantage.com.au
website ; www.lxvantage.com.au

Requirements
Must have
• Logo
• My photo
• Very corporate / professional look

```html
<!DOCTYPE html>
<html lang="en">
<head>
<meta charset="utf-8">
<title>LX Vantage – Business Card</title>
<link href="https://fonts.googleapis.com/css2?family=Quicksand:wght@400;500;600;700&display=swap" rel="stylesheet">
<style>
  :root {
    --page-bg: #e9e6e1;
    --card-black: #0b0b0c;
    --card-sheen: #1c1d20;
    --brand-blue: #29a9e0;
    --brand-blue-deep: #1a86c2;
    --text-white: #f4f6f8;
    --text-soft: #d8dde2;
  }
  * { box-sizing: border-box; margin: 0; padding: 0; }
  html, body {
    width: 1200px; height: 1022px; overflow: hidden;
    background: var(--page-bg);
    font-family: "Quicksand", "Trebuchet MS", sans-serif;
  }
  .stage {
    width: 1200px; height: 1022px;
    display: flex; align-items: center; justify-content: center;
  }
  .card {
    position: relative;
    width: 900px; height: 514px;
    border-radius: 18px;
    background: linear-gradient(160deg, var(--card-sheen) 0%, var(--card-black) 45%, var(--card-black) 100%);
    box-shadow: 0 18px 40px rgba(0,0,0,.25);
    overflow: hidden;
    color: var(--text-white);
  }
  .brand {
    position: absolute; left: 64px; top: 92px;
    display: flex; align-items: center; gap: 16px;
  }
  .brand-mark {
    width: 34px; height: 34px; background: var(--brand-blue);
  }
  .brand-name {
    font-weight: 700; font-size: 58px; letter-spacing: 1px;
    color: var(--text-white); line-height: 1;
  }
  .photo-frame {
    position: absolute; left: 590px; top: 40px;
    width: 270px; height: 230px;
    border: 1.5px solid var(--brand-blue);
  }
  .photo {
    position: absolute; left: 614px; top: 70px;
    width: 246px; height: 200px;
    background: linear-gradient(180deg, #5b3a2e 0%, #b07a62 45%, #1f63b4 100%);
  }
  .tagline-band {
    position: absolute; left: 0; top: 250px;
    width: 860px; height: 52px;
    background: var(--brand-blue);
    display: flex; align-items: center;
    padding-left: 64px;
  }
  .tagline-band::before, .tagline-band::after {
    content: ""; position: absolute; left: 0; width: 40px; height: 3px;
    background: var(--brand-blue-deep);
  }
  .tagline-band::before { bottom: -6px; }
  .tagline-band::after { bottom: -11px; }
  .tagline {
    font-size: 25px; font-weight: 500; letter-spacing: 1px;
    text-transform: uppercase; color: var(--text-white);
  }
  .contact-block {
    position: absolute; left: 64px; top: 322px;
  }
  .person-name {
    font-size: 38px; font-weight: 700; color: var(--brand-blue); line-height: 1.1;
  }
  .person-title {
    font-size: 20px; font-weight: 500; color: var(--text-soft); margin-top: 2px;
  }
  .contact-list { list-style: none; margin-top: 12px; }
  .contact-item {
    display: flex; align-items: center; gap: 14px;
    font-size: 21px; font-weight: 500; color: var(--text-white);
    line-height: 1.55;
  }
  .contact-icon { width: 16px; height: 16px; flex: none; }
</style>
</head>
<body>
<main class="stage">
  <article class="card">
    <div class="brand">
      <span class="brand-mark"></span>
      <span class="brand-name">LX Vantage</span>
    </div>

    <div class="photo-frame"></div>
    <div class="photo" role="img" aria-label="Portrait photo of Marcia Kellaway"></div>

    <div class="tagline-band">
      <p class="tagline">Develop your Rent Roll to Perform</p>
    </div>

    <section class="contact-block">
      <h1 class="person-name">Marcia Kellaway</h1>
      <p class="person-title">Property Management Consultant</p>
      <ul class="contact-list">
        <li class="contact-item">
          <svg class="contact-icon" viewBox="0 0 16 16" aria-hidden="true"><path d="M3 1.5l3 3-1.6 1.8a9 9 0 0 0 5.3 5.3L11.5 10l3 3-1.8 1.8C7.5 14.5 1.5 8.5 1.2 3.3z" fill="none" stroke="#29a9e0" stroke-width="1.5"/></svg>
          <span>+61 438592716</span>
        </li>
        <li class="contact-item">
          <svg class="contact-icon" viewBox="0 0 16 16" aria-hidden="true"><rect x="1.5" y="3" width="13" height="10" fill="none" stroke="#29a9e0" stroke-width="1.5"/><path d="M1.5 3.5l6.5 5 6.5-5" fill="none" stroke="#29a9e0" stroke-width="1.5"/></svg>
          <span>marcia@lxvantage.com.au</span>
        </li>
        <li class="contact-item">
          <svg class="contact-icon" viewBox="0 0 16 16" aria-hidden="true"><circle cx="8" cy="8" r="6.5" fill="none" stroke="#29a9e0" stroke-width="1.5"/><path d="M1.5 8h13M8 1.5c-3 3.5-3 9.5 0 13M8 1.5c3 3.5 3 9.5 0 13" fill="none" stroke="#29a9e0" stroke-width="1.2"/></svg>
          <span>www.lxvantage.com.au</span>
        </li>
      </ul>
    </section>
  </article>
</main>
</body>
</html>
```